Lantern Marketing Group (LMG)

This is for my business cards. I want a Nice anfd Elegant Business Card to be Designed, Using more or less of the same colors of my logo that i have attached.i would like to have these business cards forever

Thank you

Thank you

Thank you

Contact Information for Business Card

Tobias Rennard
Lantern Marketing Group
C.(555) 214-6083
E-Mail. TRennard@lanternmgroup.example

Font styles to use
Serif
Sans Serif

Colors
d0dfed
cbcbcb
cee9f5

Requirements
Must have
• (LMG)
• Lantern Marketing Group
Nice to have
• 3D affects
Should not have
• Please try not using the flat version of the logo try and use the 3d version please

```html
<!DOCTYPE html>
<html lang="en">
<head>
<meta charset="utf-8">
<title>Lantern Marketing Group – Business Card</title>
<link href="https://fonts.googleapis.com/css2?family=Open+Sans:wght@400;600&display=swap" rel="stylesheet">
<style>
  :root {
    --backdrop: #2b2e33;
    --slate-dark: #1e2a35;
    --slate-light: #3f4c58;
    --brand-blue: #2f6c9f;
    --brand-steel: #5b8fc2;
    --paper: #ffffff;
    --paper-shade: #f1f2f3;
    --ink: #1d1d1f;
    --rule: #cbcbcb;
  }
  * { margin: 0; padding: 0; box-sizing: border-box; }
  html, body {
    width: 1200px; height: 864px; overflow: hidden;
    background: var(--backdrop);
    font-family: "Open Sans", Arial, sans-serif;
  }
  .canvas {
    position: relative; width: 1200px; height: 864px;
  }
  .card {
    position: absolute; left: 320px; width: 560px; height: 320px;
  }
  /* Back of card */
  .card-back {
    top: 80px;
    background: linear-gradient(135deg, var(--slate-dark) 0%, var(--slate-light) 100%);
    display: flex; flex-direction: column; align-items: center; justify-content: center;
    gap: 14px;
  }
  .brand-mark {
    width: 58px; height: 58px; background: var(--brand-steel);
  }
  .brand-name {
    color: var(--brand-steel); font-weight: 600;
    font-size: 26px; letter-spacing: 3px; text-transform: uppercase;
  }
  /* Front of card */
  .card-front {
    top: 464px;
    background: radial-gradient(ellipse at 35% 50%, var(--paper) 40%, var(--paper-shade) 100%);
  }
  .front-logo {
    position: absolute; top: 34px; right: 40px;
    display: flex; align-items: center; gap: 10px;
  }
  .front-logo .brand-mark { width: 34px; height: 34px; background: var(--brand-blue); }
  .front-logo .brand-name { font-size: 34px; letter-spacing: 2px; color: var(--brand-blue); }
  .holder {
    position: absolute; left: 40px; top: 104px;
  }
  .holder-name {
    color: var(--brand-blue); font-weight: 600; font-size: 22px; line-height: 1.1;
  }
  .holder-title {
    color: var(--ink); font-size: 13px; margin-top: 2px;
  }
  .divider {
    position: absolute; left: 190px; right: 40px; top: 150px;
    height: 1px; background: var(--rule);
  }
  .contacts {
    position: absolute; right: 40px; top: 168px;
    list-style: none; text-align: right;
  }
  .contacts li {
    display: flex; justify-content: flex-end; align-items: center; gap: 10px;
    font-size: 14.5px; color: var(--ink); height: 24px;
  }
  .contact-icon {
    width: 17px; height: 17px; background: var(--brand-blue); border-radius: 2px;
    display: flex; align-items: center; justify-content: center;
  }
  .contact-icon svg { width: 11px; height: 11px; }
</style>
</head>
<body>
<main class="canvas">
  <section class="card card-back" aria-label="Card back">
    <div class="brand-mark" aria-hidden="true"></div>
    <div class="brand-name">Lantern Marketing Group</div>
  </section>

  <section class="card card-front" aria-label="Card front">
    <div class="front-logo">
      <div class="brand-mark" aria-hidden="true"></div>
      <div class="brand-name">LMG</div>
    </div>
    <div class="holder">
      <div class="holder-name">Tobias Rennard</div>
      <div class="holder-title">Managing Director</div>
    </div>
    <div class="divider"></div>
    <ul class="contacts">
      <li>(555) 214-6083
        <span class="contact-icon"><svg viewBox="0 0 12 12"><path d="M1 4 Q6 0 11 4 L9 6 L8 4.5 L4 4.5 L3 6 Z M2.5 7 H9.5 V11 H2.5 Z" fill="#fff"/></svg></span></li>
      <li>(555) 214-6091
        <span class="contact-icon"><svg viewBox="0 0 12 12"><rect x="1.5" y="4" width="9" height="7" fill="#fff"/><rect x="3.5" y="1" width="5" height="3" fill="none" stroke="#fff"/></svg></span></li>
      <li>(555) 214-6075
        <span class="contact-icon"><svg viewBox="0 0 12 12"><rect x="3" y="0.5" width="6" height="11" rx="1" fill="none" stroke="#fff" stroke-width="1.2"/><circle cx="6" cy="9.5" r="0.8" fill="#fff"/></svg></span></li>
      <li>TRennard@lanternmgroup.example
        <span class="contact-icon"><svg viewBox="0 0 12 12"><rect x="1" y="2.5" width="10" height="7" fill="none" stroke="#fff" stroke-width="1.2"/><path d="M1 2.5 L6 6.5 L11 2.5" fill="none" stroke="#fff" stroke-width="1.2"/></svg></span></li>
      <li>www.lanternmgroup.example
        <span class="contact-icon"><svg viewBox="0 0 12 12"><path d="M5 7 L7 5 M4.5 5.5 L3 7 A1.8 1.8 0 0 0 5 9 L6.5 7.5 M7.5 6.5 L9 5 A1.8 1.8 0 0 0 7 3 L5.5 4.5" fill="none" stroke="#fff" stroke-width="1.2" stroke-linecap="round"/></svg></span></li>
    </ul>
  </section>
</main>
</body>
</html>
```